Bright Path Mentors Needs A New Website Design

We need a 8 page website designed for "Bright Path Mentors .ca" similar in design to: "quill ridge learning .com".

The winner/successful candidate on the home page will be asked to complete the following inner pages to complete the project:

About Us
Philosophy
How We Work
Work With Us
Blog
Find A Tutor
Contact

Target Market(s)

Tutoring business clients/children

Industry/Entity Type

Education

Number of Pages Required

5+ page

Font styles to use
Sans Serif

Requirements
Must have
• The attached logo included of course. Similar design to the design provided above in the brief. Clear high quality high resolution images of children in school settings.

```html
<!DOCTYPE html>
<html lang="en">
<head>
<meta charset="utf-8">
<title>Bright Path Mentors</title>
<link rel="stylesheet" href="https://fonts.googleapis.com/css2?family=Cinzel:wght@400;700&family=Lato:wght@400;700&display=swap">
<style>
:root{
  --orange:#f7941d;
  --orange-dark:#e07b0a;
  --blue:#2e3a9c;
  --blue-mid:#3c4bb4;
  --navy:#1f2766;
  --ink:#333;
  --muted:#666;
  --light:#efefef;
  --dark:#2a2a2a;
  --footer:#333333;
  --white:#fff;
}
*{box-sizing:border-box;margin:0;padding:0}
html,body{width:1200px;height:3020px;overflow:hidden}
body{position:relative;font-family:'Lato',sans-serif;color:var(--ink);background:var(--white)}
.abs{position:absolute}
.serif{font-family:'Cinzel',serif}

/* top bar + nav */
.topbar{left:0;top:0;width:1200px;height:48px;background:var(--orange)}
.locator{left:586px;top:14px;font-family:'Cinzel',serif;font-size:12px;color:var(--white);letter-spacing:1px}
.locator-input{left:710px;top:14px;width:146px;height:20px;background:var(--white);font-size:10px;color:#999;padding:4px 6px}
.locator-go{left:858px;top:14px;width:30px;height:20px;background:var(--navy);color:var(--white);font-size:11px;font-weight:700;text-align:center;line-height:20px}
.social{width:30px;height:30px;border:2px solid var(--white);border-radius:50%}
.navbar{left:0;top:48px;width:1200px;height:82px;background:var(--white);border-bottom:1px solid #ddd}
.brand{left:161px;top:6px;width:178px;height:118px;background:var(--white);display:flex;flex-direction:column;align-items:center;justify-content:center;gap:8px}
.brand-mark{width:48px;height:48px;border-radius:50%;background:var(--navy)}
.brand-name{font-family:'Cinzel',serif;font-weight:700;font-size:15px;color:var(--navy);text-align:center;line-height:1.2}
.nav a{position:absolute;top:80px;font-family:'Cinzel',serif;font-size:12.5px;color:var(--ink);text-decoration:none;letter-spacing:.5px}

/* hero */
.hero{left:0;top:130px;width:1200px;height:474px;background:linear-gradient(120deg,#9dc3d6 0%,#e8b49a 35%,#5fa97a 60%,#6fb5d0 85%,#cfe1ea 100%)}
.tagline{left:161px;top:490px;width:876px;height:42px;background:rgba(30,30,30,.72);color:var(--white);font-weight:700;font-size:28px;line-height:42px;text-align:center}
.tabs{left:161px;top:578px;width:876px;height:66px;display:flex}
.tab{flex:1;font-family:'Cinzel',serif;font-size:30px;color:var(--white);text-align:center;line-height:66px}
.tab.orange{background:var(--orange)}
.tab.blue{background:var(--blue)}

/* section titles */
.sec-title{font-family:'Cinzel',serif;font-size:26px;letter-spacing:1px;text-align:center;width:1200px;left:0}
.sec-title span{color:var(--orange)}
.rule{height:2px;background:#bbb}

/* about */
.about-title{left:161px;top:682px;font-family:'Cinzel',serif;font-size:27px;letter-spacing:1px}
.about-title span{color:var(--orange)}
.about-text{left:161px;top:760px;width:510px;font-size:12.5px;line-height:19px;color:var(--muted)}
.btn{background:var(--orange);color:var(--white);font-size:12px;text-align:center}
.about-photo{left:698px;top:700px;width:336px;height:236px;background:linear-gradient(135deg,#d9d38f,#c9b7a0 50%,#8fa4c6);box-shadow:0 4px 10px rgba(0,0,0,.25);border:6px solid var(--white)}

/* why band */
.why{left:0;top:978px;width:1200px;height:294px;background:linear-gradient(90deg,#3c46a8,#5560c4 50%,#3c46a8)}
.why-item{width:200px;text-align:center;color:var(--white);font-family:'Cinzel',serif;font-size:13px;line-height:18px;letter-spacing:.5px}
.why-item svg{display:block;margin:0 auto 14px}

/* how we work */
.how{left:0;top:1272px;width:1200px;height:504px;background:var(--light)}
.card{top:1389px;width:278px;height:338px;background:var(--orange);border-radius:10px;padding:12px}
.card-photo{width:254px;height:168px;border-radius:2px}
.card h3{font-family:'Cinzel',serif;font-size:12.5px;color:var(--navy);text-align:center;margin:14px 0 6px;font-weight:700}
.card p{font-size:12.5px;line-height:19.5px;color:var(--white)}

/* what we do */
.what{left:0;top:1776px;width:1200px;height:354px;background:linear-gradient(90deg,#cfcfd6,#e6e4e0 50%,#c6c7cf)}
.services{left:161px;top:1880px;width:876px;height:183px;display:flex;box-shadow:0 6px 12px rgba(0,0,0,.2)}
.service{flex:1;text-align:center;color:var(--white);font-family:'Cinzel',serif;font-size:11.5px;line-height:16px;padding-top:22px}
.service .ring{width:70px;height:70px;border-radius:50%;background:var(--white);border:4px solid var(--orange);margin:0 auto 16px;display:flex;align-items:center;justify-content:center}

/* blog */
.blog{left:0;top:2130px;width:1200px;height:517px;background:linear-gradient(90deg,#2b2521,#3a342f 50%,#2a2522)}
.post-photo{width:330px;height:210px;border:5px solid var(--orange)}
.avatar{width:44px;height:44px;border-radius:50%;background:#c9a58a;border:3px solid var(--orange)}
.date{width:70px;height:36px;background:var(--orange);color:var(--white);font-weight:700;font-size:18px;line-height:36px;padding-left:8px}
.date small{font-size:8px;font-weight:400}
.mini{width:28px;height:22px;background:var(--orange);color:var(--white);font-size:10px;text-align:center;line-height:22px}
.post-title{font-family:'Cinzel',serif;font-weight:700;font-size:13px;color:var(--white)}
.post-cat{font-size:11px;color:var(--orange)}
.post-text{font-size:11.5px;line-height:20px;color:#ddd;width:400px}

/* newsletter */
.newsletter{left:0;top:2647px;width:1200px;height:77px;background:var(--blue)}
.nl-icon{left:160px;top:2666px;width:38px;height:38px;border:2px solid var(--white);border-radius:50%}
.nl-label{left:236px;top:2672px;font-family:'Cinzel',serif;font-size:22px;color:var(--white);letter-spacing:1px}
.nl-input{left:521px;top:2669px;width:361px;height:35px;background:var(--white);font-size:12px;color:#666;padding:10px}
.nl-btn{left:930px;top:2672px;width:78px;height:28px;background:var(--orange);color:var(--white);font-weight:700;font-size:14px;line-height:28px;text-align:center}

/* footer */
.footer{left:0;top:2724px;width:1200px;height:256px;background:var(--footer)}
.f-title{top:2766px;font-family:'Cinzel',serif;font-size:16px;color:var(--white);letter-spacing:.5px}
.f-title span{color:var(--orange)}
.f-links{left:161px;top:2804px;list-style:none;font-size:11px;line-height:22.5px;color:#ddd}
.f-links li::before{content:"• ";color:#aaa}
.f-links li.active{color:var(--orange)}
.f-contact{left:326px;top:2794px;font-size:11px;line-height:15px;color:#ddd;width:220px}
.f-row{display:flex;align-items:center;gap:10px;margin-top:14px}
.f-map{left:606px;top:2804px;width:260px;height:149px;border:4px solid var(--white);background:linear-gradient(135deg,#d6e4c8,#eae6da 45%,#bcd3e8)}
.f-brand{left:922px;top:2806px;width:115px;text-align:center}
.f-brand .brand-mark{margin:0 auto 8px;width:54px;height:54px;background:#555}
.f-brand .brand-name{color:#ccc;font-size:13px}
.copyright{left:0;top:2980px;width:1200px;height:40px;background:var(--blue);color:var(--white);font-size:11px;text-align:center;line-height:40px}
.social-sm{width:22px;height:22px;border:1.5px solid var(--white);border-radius:50%}
</style>
</head>
<body>

<header>
  <div class="abs topbar"></div>
  <div class="abs locator">Find my location</div>
  <div class="abs locator-input">Enter postal code</div>
  <div class="abs locator-go">GO!</div>
  <div class="abs social" style="left:919px;top:9px"></div>
  <div class="abs social" style="left:961px;top:9px"></div>
  <div class="abs social" style="left:1005px;top:9px"></div>

  <div class="abs navbar"></div>
  <div class="abs brand">
    <div class="brand-mark"></div>
    <div class="brand-name">Bright Path<br>Mentors</div>
  </div>
  <nav class="nav">
    <svg class="abs" style="left:346px;top:74px" width="24" height="22" viewBox="0 0 24 22"><path d="M12 2 2 11h3v9h5v-6h4v6h5v-9h3z" fill="var(--blue)"/></svg>
    <a style="left:400px">About Us</a>
    <a style="left:503px">Philosophy</a>
    <a style="left:624px">How We Work</a>
    <a style="left:760px">Work With Us</a>
    <a style="left:900px">Blog</a>
    <a style="left:975px">Contact</a>
  </nav>
</header>

<section>
  <div class="abs hero" role="img" aria-label="Photo of four children leaning together over a school desk"></div>
  <div class="abs tagline">Tutoring Is To Replace An Empty Mind With An Open One</div>
  <div class="abs tabs">
    <div class="tab orange">Courses</div>
    <div class="tab blue">Prices</div>
    <div class="tab orange">Events</div>
    <div class="tab blue">Teachers</div>
  </div>
</section>

<section>
  <h2 class="abs about-title">About <span>Bright Path Mentor</span></h2>
  <div class="abs rule" style="left:161px;top:724px;width:310px"></div>
  <p class="abs about-text">Lorem ipsum dolor sit amet, consectetuer adipiscing elit, sed diam nonummy nibh euismod tincidunt ut laoreet dolore magna aliquam erat volutpat. Ut wisi enim ad minim veniam, quis nostrud exerci tation ullamcorper suscipit lobortis nisl ut aliquip ex ea commodo consequat. Duis autem vel eum iriure dolor in hendrerit in vulputate velit esse molestie consequat. tincidunt ut laoreet dolore magna aliquam erat volutpat. Ut wisi enim ad minim veniam, quis nostrud exerci tation ullamcorper suscipit lobortis</p>
  <div class="abs btn" style="left:161px;top:900px;width:74px;height:22px;line-height:22px">Read More</div>
  <div class="abs about-photo" role="img" aria-label="Photo of a classroom with pupils raising their hands"></div>
</section>

<section>
  <div class="abs why" role="img" aria-label="Blue tinted photo of smiling schoolchildren"></div>
  <h2 class="abs sec-title" style="top:1012px;color:var(--white)">Why Bright Path Mentor</h2>
  <div class="abs rule" style="left:500px;top:1052px;width:200px;background:rgba(255,255,255,.6)"></div>
  <div class="abs why-item" style="left:158px;top:1080px">
    <svg width="90" height="96" viewBox="0 0 90 96"><path d="M45 2 86 14v34c0 24-20 40-41 46C24 88 4 72 4 48V14z" fill="var(--orange)" stroke="#fff" stroke-width="3"/><rect x="27" y="30" width="36" height="26" rx="2" fill="none" stroke="#333" stroke-width="3"/><circle cx="45" cy="58" r="8" fill="#333"/></svg>
    Certified<br>Teachers
  </div>
  <div class="abs why-item" style="left:377px;top:1080px">
    <svg width="90" height="96" viewBox="0 0 90 96"><path d="M45 2 86 14v34c0 24-20 40-41 46C24 88 4 72 4 48V14z" fill="var(--orange)" stroke="#fff" stroke-width="3"/><path d="M45 24 22 44h6v20h12V52h10v12h12V44h6z" fill="#333"/></svg>
    Flexible In-Home<br>Tutoring
  </div>
  <div class="abs why-item" style="left:597px;top:1080px">
    <svg width="90" height="96" viewBox="0 0 90 96"><path d="M45 2 86 14v34c0 24-20 40-41 46C24 88 4 72 4 48V14z" fill="var(--orange)" stroke="#fff" stroke-width="3"/><circle cx="37" cy="36" r="8" fill="#333"/><circle cx="55" cy="38" r="7" fill="#333"/><path d="M22 62c0-10 7-16 15-16s15 6 15 16zM48 62c0-8 3-13 8-13s12 5 12 13z" fill="#333"/></svg>
    Personal<br>Attention
  </div>
  <div class="abs why-item" style="left:818px;top:1080px">
    <svg width="90" height="96" viewBox="0 0 90 96"><path d="M45 2 86 14v34c0 24-20 40-41 46C24 88 4 72 4 48V14z" fill="var(--orange)" stroke="#fff" stroke-width="3"/><path d="M26 44h8v22h-8zM38 44l8-16c4 0 6 3 5 7l-2 7h12c3 0 5 3 4 6l-4 14c-1 3-3 4-6 4H38z" fill="#333"/></svg>
    Boost Your<br>Child's Confidence
  </div>
</section>

<section>
  <div class="abs how"></div>
  <h2 class="abs sec-title" style="top:1310px">How <span>We Work</span></h2>
  <div class="abs rule" style="left:490px;top:1350px;width:220px"></div>
  <article class="abs card" style="left:161px">
    <div class="card-photo" role="img" aria-label="Photo of a tutor working one-on-one with a young boy" style="background:linear-gradient(135deg,#e9d8c8,#c79c80 50%,#a8b9c8)"></div>
    <h3>In-Home One-On-One Tutoring</h3>
    <p>Lorem ipsum dolor sit amet, consectetuer adipiscing elit, sed diam nonummy nibh euismod tincidunt ut laoreet dolore magna aliquam erat volutpat. Ut wisi enim ad minim veniam, quis nostrud...[+]</p>
  </article>
  <article class="abs card" style="left:459px">
    <div class="card-photo" role="img" aria-label="Photo of a tutor helping a girl with writing" style="background:linear-gradient(135deg,#d8cfc6,#b7857a 50%,#8a6c60)"></div>
    <h3>Semi Private Tutoring</h3>
    <p>Lorem ipsum dolor sit amet, consectetuer adipiscing elit, sed diam nonummy nibh euismod tincidunt ut laoreet dolore magna aliquam erat volutpat. Ut wisi enim ad minim veniam, quis nostrud...[+]</p>
  </article>
  <article class="abs card" style="left:757px">
    <div class="card-photo" role="img" aria-label="Photo of a teacher with a small group of pupils" style="background:linear-gradient(135deg,#d6dbe3,#c89a7e 50%,#7fa0c4)"></div>
    <h3>Group Tutoring</h3>
    <p>Lorem ipsum dolor sit amet, consectetuer adipiscing elit, sed diam nonummy nibh euismod tincidunt ut laoreet dolore magna aliquam erat volutpat. Ut wisi enim ad minim veniam, quis nostrud...[+]</p>
  </article>
</section>

<section>
  <div class="abs what" role="img" aria-label="Faded photo of schoolchildren with backpacks"></div>
  <h2 class="abs sec-title" style="top:1798px">What <span>We Do</span></h2>
  <div class="abs rule" style="left:500px;top:1838px;width:200px"></div>
  <div class="abs services">
    <div class="service" style="background:#5b6bd0"><div class="ring"><svg width="34" height="30" viewBox="0 0 34 30"><path d="M4 6 20 2l10 6-16 5zM4 6v16l10 6 16-5V8" fill="none" stroke="#333" stroke-width="3"/></svg></div>All Subjects -<br>Math, English,<br>and More!</div>
    <div class="service" style="background:#4b59c2"><div class="ring"><svg width="36" height="28" viewBox="0 0 36 28"><path d="M18 2 2 10l16 8 16-8z" fill="#333"/><path d="M8 14v8c6 4 14 4 20 0v-8" fill="#333"/></svg></div>We Work With<br>Your Student's<br>Current Class</div>
    <div class="service" style="background:#3c49b0"><div class="ring"><svg width="28" height="34" viewBox="0 0 28 34"><rect x="3" y="5" width="22" height="27" rx="2" fill="none" stroke="#333" stroke-width="3"/><path d="M8 15h12M8 21h12M8 27h8" stroke="#333" stroke-width="2.5"/></svg></div>ACT/SAT<br>Test Prep</div>
    <div class="service" style="background:#2f3c9c"><div class="ring"><svg width="36" height="30" viewBox="0 0 36 30"><circle cx="10" cy="9" r="5" fill="#333"/><circle cx="26" cy="9" r="5" fill="#333"/><circle cx="18" cy="12" r="6" fill="#333"/><path d="M6 28c0-8 5-12 12-12s12 4 12 12z" fill="#333"/></svg></div>In-Home<br>Tutoring - We<br>Come to You</div>
    <div class="service" style="background:#263187"><div class="ring"><svg width="36" height="32" viewBox="0 0 36 32"><rect x="8" y="3" width="26" height="18" fill="none" stroke="#333" stroke-width="3"/><circle cx="6" cy="16" r="4" fill="#333"/><path d="M2 30v-8h8l6-4" stroke="#333" stroke-width="3" fill="none"/></svg></div>Remedial<br>Programs</div>
    <div class="service" style="background:#1f2870"><div class="ring"><svg width="36" height="30" viewBox="0 0 36 30"><path d="M4 8c0-4 6-4 6 0v16h22V8z" fill="none" stroke="#333" stroke-width="3"/><path d="M14 14h14M14 19h10" stroke="#333" stroke-width="2.5"/></svg></div>Enrichment<br>Programs</div>
  </div>
</section>

<section>
  <div class="abs blog" role="img" aria-label="Dark photo of children studying together"></div>
  <h2 class="abs sec-title" style="top:2166px;color:var(--white)">Latest Blog</h2>
  <div class="abs rule" style="left:500px;top:2206px;width:200px;background:rgba(255,255,255,.5)"></div>

  <div class="abs avatar" style="left:169px;top:2243px" role="img" aria-label="Author photo"></div>
  <div class="abs date" style="left:167px;top:2300px">21 <small>SEP 2016</small></div>
  <div class="abs mini" style="left:208px;top:2344px">0</div>
  <div class="abs mini" style="left:208px;top:2372px">▣</div>
  <div class="abs post-photo" style="left:236px;top:2250px;background:linear-gradient(135deg,#f0efec,#e0c7b4 50%,#cfd2d6)" role="img" aria-label="Photo of a smiling girl holding up a test marked A plus"></div>
  <div class="abs post-title" style="left:232px;top:2476px">Lorem Ipsum Dolor Sit Amet</div>
  <div class="abs post-cat" style="left:232px;top:2501px">▬ &nbsp;Uncategorized</div>
  <p class="abs post-text" style="left:232px;top:2524px">Lorem ipsum dolor sit amet, consectetuer adipiscing elit, sed diam nonummy nibh euismod tincidunt</p>
  <div class="abs btn" style="left:232px;top:2580px;width:70px;height:22px;line-height:22px">Read More</div>

  <div class="abs avatar" style="left:640px;top:2243px" role="img" aria-label="Author photo"></div>
  <div class="abs date" style="left:636px;top:2300px">21 <small>SEP 2016</small></div>
  <div class="abs mini" style="left:677px;top:2344px">0</div>
  <div class="abs mini" style="left:677px;top:2372px">▣</div>
  <div class="abs post-photo" style="left:705px;top:2250px;background:linear-gradient(135deg,#cfe3ec,#d2a58d 50%,#7fb07f)" role="img" aria-label="Photo of four children around a laptop"></div>
  <div class="abs post-title" style="left:704px;top:2476px">Lorem Ipsum Dolor Sit Amet</div>
  <div class="abs post-cat" style="left:704px;top:2501px">▬ &nbsp;Uncategorized</div>
  <p class="abs post-text" style="left:704px;top:2524px">Lorem ipsum dolor sit amet, consectetuer adipiscing elit, sed diam nonummy nibh euismod tincidunt</p>
  <div class="abs btn" style="left:704px;top:2580px;width:70px;height:22px;line-height:22px">Read More</div>
</section>

<section>
  <div class="abs newsletter"></div>
  <div class="abs nl-icon"><svg width="34" height="34" viewBox="0 0 34 34"><rect x="8" y="11" width="18" height="12" fill="none" stroke="#fff" stroke-width="2"/><path d="M8 11l9 7 9-7" fill="none" stroke="#fff" stroke-width="2"/></svg></div>
  <div class="abs nl-label">Newsletter Signup ❯</div>
  <div class="abs nl-input">Your e-mail</div>
  <div class="abs nl-btn">Sign Up</div>
</section>

<footer>
  <div class="abs footer"></div>
  <h4 class="abs f-title" style="left:161px">Quick <span>Links</span></h4>
  <ul class="abs f-links">
    <li class="active">Home</li><li>About Us</li><li>Philosophy</li><li>How We Work</li><li>Work With Us</li><li>Blog</li><li>Contact</li>
  </ul>
  <h4 class="abs f-title" style="left:326px">Contact <span>Information</span></h4>
  <div class="abs f-contact">
    <strong style="color:#fff">Bright Path Mentors</strong><br>
    123, Lorem ipsum dolor sit amet,<br>consectetuer adipiscing elit, sed diamh<br>nonummy nibh euismod - 123 456
    <div class="f-row"><svg width="14" height="14" viewBox="0 0 14 14"><path d="M3 1l3 3-2 2c1 2 2 3 4 4l2-2 3 3-2 2C6 13 1 8 1 3z" fill="#ccc"/></svg>123 456 7890</div>
    <div class="f-row"><svg width="14" height="14" viewBox="0 0 14 14"><rect x="1" y="4" width="12" height="8" fill="#ccc"/><rect x="3" y="1" width="8" height="4" fill="#ccc"/></svg>123 456 7890</div>
    <div class="f-row"><svg width="14" height="14" viewBox="0 0 14 14"><rect x="1" y="3" width="12" height="8" fill="none" stroke="#ccc" stroke-width="1.5"/><path d="M1 3l6 5 6-5" fill="none" stroke="#ccc" stroke-width="1.5"/></svg>info@brightpathmentors.com</div>
  </div>
  <h4 class="abs f-title" style="left:604px">Location <span>Map</span></h4>
  <div class="abs f-map" role="img" aria-label="Street map showing the office location"></div>
  <div class="abs f-brand">
    <div class="brand-mark"></div>
    <div class="brand-name">Bright Path Mentors</div>
  </div>
  <div class="abs copyright">Copyright © 2016 Bright Path Mentors 2016. All Right Reserved.</div>
  <div class="abs social-sm" style="left:950px;top:2989px"></div>
  <div class="abs social-sm" style="left:980px;top:2989px"></div>
  <div class="abs social-sm" style="left:1010px;top:2989px"></div>
</footer>

</body>
</html>
```